Marketplace Web Re-design overhaul @corvahub

Hi,
We are currently in production with a website that is getting some mixed feedback about visual appeal and usability. We are using a responsive design and need to stay true to the logo colours and other marketing collateral we have in place. I will provide a brochure with the colour palate we use for some guidance. If you can please help us design something fresh and modern to communicate the essence of our company. The brochure will be a good summary of what we do and who we are targeting as customers. Our current website can be found at www.corvahub.com. If there is any questions, please let me know.

Target Market(s)

Contractors and Corporate Companies

Industry/Entity Type

Information Technology

Number of Pages Required

4 page

Requirements
Must have
• Must have a complete new visual look, including
• 1. Images
• 2. Background colour scheme overhaul (not black)
• 3. re-design of the layout but keep to similar page breakdowns
Nice to have
• Some of the pages are a bit wordy, happy to have suggestions on how to reduce.
• Would be great if we can integrate the Drift.ON! blog page to the Corvahub page?
• This is some feedback a fellow UX designer provided to improve our CRO
• First off when you land on the home page, who is your audience? Are you everything to everyone? Even after watching the video (https://www.vidplex-example.com/watch?v=q-RtnB7LpX3), I do not know what markets you service or who this app will be for.
• Your main headline and paragraph above the fold I find unnecessarily wordy and an overuse of 'buzzwords' . Perhaps you could look at appealing to the lowest common denominator and make it very simple and put it all into a simple sentence.
• The main hero image to the right of the headline offers no emotional pull at all. I'm assuming it's just a screenshot of your dashboard? Personally, I would be looking at using a person's image in that space.
• Also in this space, increase the size of your 'register' button. On the topic of your register button, you have it in different colours. Green in header, and red in content. Make it the same colour, and don't use that colour again on the site. That colour is to become your call to action (CTA) colour. Understandably you'll have three different colours for the account type, and again, don't use these colours anywhere else on the site.
• The registration area where the three account types are where you choose which one suits you, it's extremely busy with background images and heavy use of text. If you were my client, I would be advising you to ditch the bg image (including the iPad shot), keeping the text, making the register icons much bigger. Perhaps instead of bg images, use a solid colour for each (green, orange, red). I'm highly confident this change will make a massive difference in your sign up rate.
Should not have
• Please keep to the fonts used on the original website
• Keep to the colour provided on the company brochure for guidance.

```html
<!DOCTYPE html>
<html lang="en">
<head>
<meta charset="utf-8">
<title>Corvahub – Available Quality Talent On Demand</title>
<link rel="stylesheet" href="https://fonts.googleapis.com/css2?family=Lato:ital,wght@0,300;0,400;0,700;1,400&family=Open+Sans:wght@400;600&display=swap">
<style>
:root{
  --red:#9e1b20;
  --red-dark:#861518;
  --ink:#5b5b5b;
  --ink-dark:#333333;
  --muted:#777777;
  --nav:#333333;
  --navy:#0f3a5c;
  --navy-deep:#0b2a45;
  --black:#000000;
  --white:#ffffff;
  --orange:#f39a1e;
}
*{box-sizing:border-box;margin:0;padding:0}
html,body{width:1200px;height:2769px;overflow:hidden;background:var(--white)}
body{font-family:"Open Sans",Arial,sans-serif;color:var(--ink)}
.page{position:relative;width:1200px;height:2769px;overflow:hidden}
.abs{position:absolute}

/* header */
.site-header{left:0;top:0;width:1200px;height:72px;background:var(--white)}
.brand{left:80px;top:16px;display:flex;align-items:center;gap:12px}
.brand-dot{width:34px;height:34px;border-radius:50%;background:var(--red)}
.brand-name{font-family:"Lato",sans-serif;font-weight:400;font-size:38px;color:var(--muted);letter-spacing:.5px;line-height:1}
.search{left:899px;top:22px;width:180px;height:33px;border:1px solid #cfcfcf;background:#f4f4f4;font-size:15px;color:#555;padding:6px 10px}
.search-btn{left:1071px;top:14px;width:50px;height:50px;border-radius:50%;background:var(--red)}

/* nav */
.main-nav{left:0;top:72px;width:1200px;height:61px;background:var(--nav)}
.main-nav a{position:absolute;top:20px;transform:translateX(-50%);color:var(--white);text-decoration:none;font-family:"Lato",sans-serif;font-size:17px;white-space:nowrap}

/* hero */
.hero{left:0;top:133px;width:1200px;height:625px;background:linear-gradient(135deg,#cfd3d8 0%,#eef0f2 40%,#f7f7f7 60%,#b9bec5 100%)}

/* welcome */
.welcome{left:0;top:758px;width:1200px;height:364px;text-align:center}
.welcome h1{position:absolute;left:0;width:1200px;top:45px;font-family:"Lato",sans-serif;font-weight:400;font-size:54px;color:var(--ink);letter-spacing:1px}
.welcome .tagline{position:absolute;left:0;width:1200px;top:108px;font-size:16px;color:var(--red)}
.welcome p.intro{position:absolute;left:160px;width:880px;top:147px;font-size:15.5px;line-height:24px;color:var(--muted)}
.btn-more{left:526px;top:254px;width:148px;height:55px;background:var(--red);border-radius:4px;color:var(--white);font-family:"Lato",sans-serif;font-size:25px;line-height:55px;text-align:center}

/* features */
.features{left:0;top:1122px;width:1200px;height:468px;background:linear-gradient(135deg,var(--navy-deep) 0%,#175079 50%,var(--navy-deep) 100%)}
.features h2{position:absolute;left:0;width:1200px;top:48px;text-align:center;font-family:"Lato",sans-serif;font-weight:400;font-size:32px;color:var(--white)}
.feature-card{top:141px;width:292px;height:260px;border:1.5px solid rgba(255,255,255,.85);text-align:center;color:var(--white)}
.feature-card svg{position:absolute;left:50%;top:28px;transform:translateX(-50%)}
.feature-card h3{position:absolute;left:0;width:100%;top:110px;font-family:"Lato",sans-serif;font-weight:400;font-size:22px}
.feature-card p{position:absolute;left:20px;width:252px;top:148px;font-size:15px;line-height:25px}

/* blog */
.blog{left:0;top:1590px;width:1200px;height:397px}
.blog h2{position:absolute;left:80px;top:53px;font-family:"Lato",sans-serif;font-weight:400;font-size:33px;color:var(--ink-dark)}
.blog-thumb{position:absolute}
.blog-title{position:absolute;font-family:"Lato",sans-serif;font-size:21px;color:var(--ink)}
.blog-text{position:absolute;font-size:15px;line-height:25px;color:var(--muted)}
.blog-date{position:absolute;font-family:"Lato",sans-serif;font-style:italic;font-size:15px;color:var(--muted)}

/* team */
.team{left:0;top:1987px;width:1200px;height:416px;background:linear-gradient(180deg,#5c5a55 0%,#3f3d3a 60%,#2a2927 100%)}
.team h2{position:absolute;left:0;width:1200px;top:48px;text-align:center;font-family:"Lato",sans-serif;font-weight:400;font-size:36px;color:var(--white)}
.member{position:absolute;top:115px;width:300px;margin-left:-150px;text-align:center;color:var(--white)}
.portrait{width:126px;height:126px;border-radius:50%;border:3px solid var(--white);margin:0 auto;background:linear-gradient(160deg,#d9c2b1,#8e7b6f)}
.member .name{margin-top:14px;font-family:"Lato",sans-serif;font-size:21px}
.member .role{margin-top:6px;font-size:15px}
.slider-arrow{position:absolute;top:2159px;width:42px;height:42px;border-radius:50%;background:var(--white)}
.slider-arrow svg{display:block}

/* newsletter */
.newsletter{left:78px;top:2330px;width:1044px;height:186px;background:var(--red)}
.newsletter h2{position:absolute;left:0;width:100%;top:40px;text-align:center;font-family:"Lato",sans-serif;font-weight:400;font-size:32px;color:var(--white)}
.field{position:absolute;top:92px;height:42px;border:1.5px solid rgba(255,255,255,.9);color:var(--white);font-size:15px;padding:10px}
.btn-subscribe{position:absolute;left:707px;top:92px;width:177px;height:42px;background:var(--black);color:var(--white);font-family:"Lato",sans-serif;font-size:21px;line-height:42px;text-align:center}

/* footer */
.site-footer{left:0;top:2403px;width:1200px;height:366px;background:var(--black);z-index:-0}
.footer-head{position:absolute;font-family:"Lato",sans-serif;font-size:18px;color:var(--white)}
.footer-item{position:absolute;display:flex;align-items:flex-start;gap:20px;font-size:15px;line-height:24px;color:var(--white)}
.partner-badge{position:absolute;top:2608px;height:62px}
.copyright{left:0;top:2716px;width:1200px;text-align:center;font-size:15px;color:var(--white)}
.copyright strong{color:var(--orange)}
</style>
</head>
<body>
<div class="page">

  <header class="site-header abs">
    <div class="brand abs"><span class="brand-dot"></span><span class="brand-name">corvahub</span></div>
    <div class="search abs">Search here..</div>
    <div class="search-btn abs">
      <svg width="50" height="50" viewBox="0 0 50 50" aria-hidden="true"><circle cx="23" cy="23" r="7" fill="none" stroke="#fff" stroke-width="3"/><line x1="28" y1="28" x2="33" y2="33" stroke="#fff" stroke-width="3.5" stroke-linecap="round"/></svg>
    </div>
  </header>

  <nav class="main-nav abs">
    <a style="left:246px">HOME</a>
    <a style="left:395px">HOW IT WORKS</a>
    <a style="left:561px">ABOUT US</a>
    <a style="left:722px">OUR PARTNERS</a>
    <a style="left:858px">FAQS</a>
    <a style="left:956px">BLOG</a>
  </nav>

  <div class="hero abs" role="img" aria-label="Overhead view of a team working together at a white desk with laptops, lamps and a tablet"></div>

  <section class="welcome abs">
    <h1>WELCOME</h1>
    <div class="tagline">Available Quality Talent On Demand</div>
    <p class="intro">Corvahub is a unique marketplace providing contractors and companies a platform to connect in real-time by exposing the “availability status”. Through intuitive search Corvahub will instantly shortlist available contractors with matching skill criteria. This is an invaluable tool for companies finding the right people at the right time and at low cost!!</p>
    <div class="btn-more abs">MORE</div>
  </section>

  <section class="features abs">
    <h2>THE FUTURE OF WORK IS HERE !</h2>
    <div class="feature-card abs" style="left:79px">
      <svg width="64" height="56" viewBox="0 0 64 56" aria-hidden="true" fill="none" stroke="#fff" stroke-width="2.5" stroke-linejoin="round"><path d="M14 4h36l12 14L32 52 2 18z"/><path d="M2 18h60M24 4l-6 14 14 34 14-34-6-14"/></svg>
      <h3>SKILLS MATCH</h3>
      <p>Corvahub has a secret sauce to find the right people to match the job requirements, put your roles.</p>
    </div>
    <div class="feature-card abs" style="left:452px">
      <svg width="62" height="58" viewBox="0 0 62 58" aria-hidden="true"><rect x="2" y="8" width="46" height="42" rx="4" fill="none" stroke="#fff" stroke-width="3"/><rect x="2" y="8" width="46" height="10" fill="#fff"/><rect x="12" y="2" width="4" height="10" fill="#fff"/><rect x="34" y="2" width="4" height="10" fill="#fff"/><g fill="#fff"><rect x="9" y="24" width="7" height="6"/><rect x="21" y="24" width="7" height="6"/><rect x="9" y="35" width="7" height="6"/><rect x="21" y="35" width="7" height="6"/></g><circle cx="46" cy="42" r="13" fill="#14466c" stroke="#fff" stroke-width="3"/><path d="M46 35v8h6" fill="none" stroke="#fff" stroke-width="3"/></svg>
      <h3>CALENDER</h3>
      <p>Corvahub has a secret sauce to find the right people to match the job requirements, put your roles.</p>
    </div>
    <div class="feature-card abs" style="left:829px">
      <svg width="44" height="60" viewBox="0 0 44 60" aria-hidden="true"><path d="M22 2C11 2 2 11 2 22c0 15 20 36 20 36s20-21 20-36C42 11 33 2 22 2z" fill="#fff"/><circle cx="22" cy="21" r="7" fill="#14466c"/></svg>
      <h3>LOCATION</h3>
      <p>Corvahub has a secret sauce to find the right people to match the job requirements, put your roles.</p>
    </div>
  </section>

  <section class="blog abs">
    <h2>RECENT BLOG</h2>
    <div class="blog-thumb" style="left:76px;top:105px;width:286px;height:229px;background:linear-gradient(160deg,#cfe3f3,#7ea6c8 60%,#4d7aa3)" role="img" aria-label="Business people silhouetted against a bright office window"></div>
    <div class="blog-title" style="left:377px;top:103px">The Best Tech</div>
    <div class="blog-text" style="left:377px;top:147px;width:265px">Job hunting this year? Here are the tech skills hiring managers want to see on your résumé. It may be obvious to some, but it's important that tech skills align with the current demands of our time.</div>
    <div class="blog-date" style="left:377px;top:310px">3 march 2015</div>

    <div class="blog-thumb" style="left:661px;top:105px;width:103px;height:100px;background:linear-gradient(135deg,#f4f4f4,#e2d8cc)" role="img" aria-label="Hands working on a desk with papers and devices"></div>
    <div class="blog-title" style="left:785px;top:103px">Top five cloud skills</div>
    <div class="blog-text" style="left:785px;top:136px;width:350px">Job hunting this year? Here are the tech skills hiring managers want to see on your résumé. ..</div>
    <div class="blog-date" style="left:785px;top:188px">3 march 2015</div>

    <div class="blog-thumb" style="left:661px;top:239px;width:103px;height:102px;background:linear-gradient(135deg,#9fe0f0,#2fb2d6)" role="img" aria-label="Laptop on a bright blue background"></div>
    <div class="blog-title" style="left:785px;top:238px">20 hot IT skills</div>
    <div class="blog-text" style="left:785px;top:271px;width:350px">Job hunting this year? Here are the tech skills hiring managers want to see on your résumé. ..</div>
    <div class="blog-date" style="left:785px;top:323px">3 march 2015</div>
  </section>

  <footer class="site-footer abs">
    <div class="footer-head" style="left:78px;top:155px">Contact Us</div>
    <div class="footer-item" style="left:78px;top:208px">
      <svg width="14" height="20" viewBox="0 0 14 20" aria-hidden="true"><path d="M7 0C3 0 0 3 0 7c0 5 7 13 7 13s7-8 7-13c0-4-3-7-7-7z" fill="#fff"/><circle cx="7" cy="7" r="2.5" fill="#000"/></svg>
      <span>Lorem ipsum dolor sit amet,<br>consectetuer adipi&nbsp;elit.</span>
    </div>
    <div class="footer-head" style="left:515px;top:155px">Get in touch</div>
    <div class="footer-item" style="left:515px;top:208px">
      <svg width="18" height="18" viewBox="0 0 18 18" aria-hidden="true"><path d="M3 1l4 3-2 3c1 2 3 4 5 5l3-2 3 4-3 3C7 17 1 11 0 4z" fill="#fff"/></svg>
      <span>555-010-2468</span>
    </div>
    <div class="footer-item" style="left:515px;top:249px">
      <svg width="20" height="16" viewBox="0 0 20 16" aria-hidden="true" fill="none" stroke="#fff" stroke-width="1.8"><rect x="1" y="1" width="18" height="14" rx="2"/><path d="M1 3l9 7 9-7"/></svg>
      <span>info@corvahub.com</span>
    </div>
    <div class="footer-head" style="left:818px;top:150px">Our strategic partners</div>
    <div class="copyright abs" style="top:313px"><strong>© THE CORVAHUB</strong> -2016.All Rights Reserved.</div>
  </footer>

  <div class="partner-badge" style="left:814px;width:124px;background:#e5252e" role="img" aria-label="Partner badge"></div>
  <div class="partner-badge" style="left:975px;width:145px;background:#3a7fb0;border-radius:4px" role="img" aria-label="Partner badge"></div>

  <section class="team abs">
    <h2>MEET OUR TEAM</h2>
    <div class="member" style="left:292px">
      <div class="portrait" role="img" aria-label="Portrait of Maren Holloway"></div>
      <div class="name">Maren Holloway</div>
      <div class="role">CEO &amp; Co-Founder</div>
    </div>
    <div class="member" style="left:591px">
      <div class="portrait" role="img" aria-label="Portrait of Dario Venturi"></div>
      <div class="name">Dario Venturi</div>
      <div class="role">CTO &amp; Co-Founder</div>
    </div>
    <div class="member" style="left:886px">
      <div class="portrait" role="img" aria-label="Portrait of Glen Ashford"></div>
      <div class="name">Glen Ashford</div>
      <div class="role">COO &amp; Advisory Board Member</div>
    </div>
  </section>
  <div class="slider-arrow" style="left:77px"><svg width="42" height="42" viewBox="0 0 42 42" aria-hidden="true"><path d="M24 14l-7 7 7 7" fill="none" stroke="#555" stroke-width="2"/></svg></div>
  <div class="slider-arrow" style="left:1079px"><svg width="42" height="42" viewBox="0 0 42 42" aria-hidden="true"><path d="M18 14l7 7-7 7" fill="none" stroke="#555" stroke-width="2"/></svg></div>

  <section class="newsletter abs">
    <h2>NEWS LETTER</h2>
    <div class="field" style="left:180px;width:252px">Name</div>
    <div class="field" style="left:441px;width:251px">Email</div>
    <div class="btn-subscribe">SUBSCRIBE</div>
  </section>

</div>
</body>
</html>
```